依頼詳細
TOPページのイメージは変更せずに、最近導入したVRでの物件紹介や販売物件のページを増やしたい。VRのコンテンツについては、URLを組み込めるので、自社でカスタマイズできるようにしてほしい。
また、現在のTOPページを超える斬新なデザインを提案していただければ採用も検討します。
サイトURL
http://k-t-r.jp
ページ数
2ページ
希望イメージ
シンプル 複雑
単色 カラフル
暗い 明るい
日常 高級
遊び心 厳粛
未来的 伝統的
女性的 男性的
希望する色
納品ファイル
補足説明
以前に別法人のロゴをコンペ形式で募集した内容です。
参考までに↓
https://www.sakumado.jp/work/detail/417352
依頼金額を99320円に変更して、延長しました。
提案者が少なすぎて残念に思っております。
漠然とし過ぎた依頼なのかもしれませんが、デザイン性だけでも比較してみたいのが理由です。
期限時間ギリギリで1件の応募で、キャンセルするにしても全額お一人だけに配分することが納得いきませんので、何人かに配分出来ればと思い延長させて頂きました。
同じ方からの度重なる提案は受け入れ難く思っております。
これぞという提案でご参加いただきますようご配慮くださいませ。
仙台の街並み等の風景は個人的に好きではありません。
仙台が本社ではありますが、商圏は全国ですのであまり仙台を意識しないデザインでお願いします。

細かい部分はさておき、私の好みをなんとなく汲み取って頂いたようなので選ばせていただきました。

ご提案頂いた皆様ありがとうございました。

```html
<!DOCTYPE html>
<html lang="ja">
<head>
<meta charset="utf-8">
<title>KEYTOWN 不動産</title>
<link href="https://fonts.googleapis.com/css2?family=Noto+Sans+JP:wght@400;500;700;900&display=swap" rel="stylesheet">
<style>
:root{
  --blue:#2a6fc0;
  --blue-dark:#1d5aa3;
  --ink:#333;
  --muted:#777;
  --line:#e2e2e2;
  --green:#5c9f3c;
  --green-soft:#eef7e6;
  --hero:#eeeff1;
  --footer:#f3f3f3;
}
*{box-sizing:border-box;margin:0;padding:0}
html,body{width:718px;height:1200px;overflow:hidden;background:#fff}
body{font-family:"Noto Sans JP",sans-serif;color:var(--ink);position:relative}
.site-header{position:absolute;left:0;top:0;width:718px;height:52px;background:#fff;border-bottom:1px solid var(--line)}
.brand{position:absolute;left:72px;top:14px;font-weight:900;font-size:20px;letter-spacing:1px;color:#222}
.global-nav{position:absolute;left:250px;top:0;display:flex;height:52px}
.global-nav a{font-size:9px;color:#444;text-decoration:none;padding:0 10px;line-height:24px;height:24px;margin-top:1px}
.global-nav a.current{border-bottom:2px solid var(--blue)}
.hero{position:absolute;left:0;top:52px;width:718px;height:231px;background:var(--hero);overflow:hidden}
.hero-photo{position:absolute;right:0;top:0;width:430px;height:231px;background:linear-gradient(90deg,rgba(238,239,241,1) 0%,#c9ccd1 35%,#9fa3aa 70%,#7d828a 100%)}
.hero-title{position:absolute;left:72px;top:100px;font-size:21px;font-weight:700;color:#222}
.hero-sub{position:absolute;left:72px;top:132px;font-size:9px;color:#444}
.hero-btn{position:absolute;left:72px;top:186px;width:86px;height:24px;border:1px solid #333;font-size:9px;line-height:22px;text-align:center;color:#222;background:#fff}
.features{position:absolute;left:72px;top:312px;width:383px;display:flex;justify-content:space-between}
.feature{width:118px;text-align:center}
.feature-icon{width:48px;height:48px;border-radius:50%;background:#fff;border:1px solid #d8dde5;margin:0 auto 10px;display:flex;align-items:center;justify-content:center}
.feature h3{font-size:10px;font-weight:700;color:var(--blue-dark);margin-bottom:8px}
.feature p{font-size:7.5px;line-height:1.6;color:var(--muted);text-align:left}
.vr-viewer{position:absolute;left:77px;top:495px;width:372px;height:193px;background:linear-gradient(180deg,#8e8a80 0%,#c9c0ae 40%,#a89a82 70%,#5d564c 100%)}
.post{position:absolute;left:77px;top:718px;width:378px;height:76px;border-top:1px solid var(--line);border-bottom:1px solid var(--line);padding-top:10px}
.post-thumb{position:absolute;left:0;top:10px;width:72px;height:58px;background:linear-gradient(135deg,#d9dde3,#9aa2ad)}
.post-date{position:absolute;left:90px;top:12px;font-size:8px;color:var(--muted)}
.post-title{position:absolute;left:90px;top:28px;font-size:11px;font-weight:500}
.post-excerpt{position:absolute;left:90px;top:46px;font-size:7.5px;color:var(--muted)}
.post-badge{position:absolute;right:0;top:12px;background:var(--blue);color:#fff;font-size:7px;padding:2px 8px}
.sidebar{position:absolute;left:498px;top:318px;width:154px}
.contact-box{border:1px solid var(--line);padding:10px 10px 12px;text-align:center}
.contact-box .lead{font-size:8px;line-height:1.5;color:#444}
.contact-box .tel{font-size:17px;font-weight:900;color:var(--blue-dark);margin-top:4px;line-height:1.1}
.contact-box .hours{font-size:6.5px;color:var(--muted);margin-top:4px;line-height:1.5}
.contact-btn{display:block;margin-top:8px;background:var(--blue);color:#fff;font-size:9px;padding:8px 0;border-radius:3px}
.side-menu{list-style:none;margin-top:18px;border-top:1px solid var(--line)}
.side-menu li{font-size:8px;color:#444;padding:6px 4px;border-bottom:1px solid var(--line)}
.side-menu li.sub{padding-left:14px}
.rule{position:absolute;left:0;top:858px;width:718px;border-top:1px solid var(--line)}
.listing-label{position:absolute;left:72px;font-size:10px;font-weight:700;color:#333}
.listing-table{position:absolute;left:72px;width:580px;border-collapse:collapse;table-layout:fixed}
.listing-table td{border:1px solid var(--green);height:40px;font-size:7.5px;text-align:center;color:#333;line-height:1.3}
.listing-table td.head{background:#fff;font-weight:500}
.listing-table td{background:var(--green-soft)}
.site-footer{position:absolute;left:0;top:1055px;width:718px;height:145px;background:var(--footer);border-top:2px solid var(--blue)}
.copyright{position:absolute;top:80px;width:718px;text-align:center;font-size:7px;color:#555}
.powered{position:absolute;top:95px;width:718px;text-align:center;font-size:7px;color:#777}
.to-top{position:absolute;left:676px;top:1136px;width:22px;height:22px;background:#444;border-radius:2px;display:flex;align-items:center;justify-content:center}
</style>
</head>
<body>
<header class="site-header">
  <div class="brand">KEYTOWN</div>
  <nav class="global-nav">
    <a class="current">ホーム</a><a>VR案内コーナー</a><a>お部屋探しの手順</a><a>オーナー様へ</a><a>お問い合わせ</a><a>recruit</a>
  </nav>
</header>

<section class="hero">
  <div class="hero-photo" role="img" aria-label="VRゴーグルを着けて物件を体験する様子の写真"></div>
  <h1 class="hero-title">VRによる物件案内</h1>
  <p class="hero-sub">臨場感のあるご紹介が可能です</p>
  <div class="hero-btn">READ MORE</div>
</section>

<section class="features">
  <div class="feature">
    <div class="feature-icon"><svg width="22" height="22" viewBox="0 0 22 22" fill="none" stroke="#2a6fc0" stroke-width="1.8"><path d="M4 5h2M4 11h2M4 17h2M9 5h9M9 11h9M9 17h9"/></svg></div>
    <h3>お部屋探しの手順</h3>
    <p>お部屋探しの手順についてのテキストが入ります。初めての方にも分かりやすくご案内するための説明文です。</p>
  </div>
  <div class="feature">
    <div class="feature-icon"><svg width="24" height="22" viewBox="0 0 24 22" fill="none" stroke="#2a6fc0" stroke-width="1.8"><rect x="2" y="6" width="20" height="10" rx="3"/><circle cx="8" cy="11" r="2"/><circle cx="16" cy="11" r="2"/></svg></div>
    <h3>VRによる物件案内</h3>
    <p>VRによる物件案内についてのテキストが入ります。現地に行かずに室内を見学できる仕組みの説明です。</p>
  </div>
  <div class="feature">
    <div class="feature-icon"><svg width="22" height="22" viewBox="0 0 22 22" fill="#2a6fc0"><circle cx="11" cy="7" r="4"/><path d="M3 20c0-5 4-7 8-7s8 2 8 7z"/></svg></div>
    <h3>オーナー様へ</h3>
    <p>オーナー様へ向けてのテキストが入ります。物件の管理や募集に関するご相談について説明します。</p>
  </div>
</section>

<div class="vr-viewer" role="img" aria-label="室内を360度見渡せるVRパノラマビュー"></div>

<article class="post">
  <div class="post-thumb" role="img" aria-label="VR案内コーナーの記事サムネイル写真"></div>
  <div class="post-date">2019年7月9日</div>
  <h2 class="post-title">VR案内コーナー</h2>
  <p class="post-excerpt">VRでご覧いただける物件のご案内</p>
  <span class="post-badge">VR案内</span>
</article>

<aside class="sidebar">
  <div class="contact-box">
    <p class="lead">お気軽にお問い合わせ<br>ください。</p>
    <p class="tel">022-<br>555-0184</p>
    <p class="hours">受付時間 10:00-18:00<br>[ 定休日 水曜日 ]</p>
    <span class="contact-btn">✉ お問い合わせ</span>
  </div>
  <ul class="side-menu">
    <li>ホーム</li>
    <li>VR案内コーナー</li>
    <li>お部屋探しの手順</li>
    <li class="sub">プラン集</li>
    <li class="sub">ご利用の流れ</li>
    <li>オーナー様へ</li>
    <li>お問い合わせ</li>
    <li>recruit</li>
  </ul>
</aside>

<div class="rule"></div>

<h2 class="listing-label" style="top:876px">マンション・アパート</h2>
<table class="listing-table" style="top:896px">
  <tr><td class="head">マンション<br>アパート</td><td>一戸建て</td><td>土地</td><td>店舗<br>事務所</td><td>ビル</td><td>駐車場</td></tr>
</table>

<h2 class="listing-label" style="top:964px">賃貸物件</h2>
<table class="listing-table" style="top:984px">
  <tr><td class="head">マンション<br>アパート</td><td>一戸建て</td><td>土地</td><td>店舗<br>事務所</td><td>ビル</td><td>駐車場</td></tr>
</table>

<footer class="site-footer">
  <p class="copyright">Copyright © KEYTOWN 不動産 All Rights Reserved.</p>
  <p class="powered">Powered by SiteFrame with Horizon Theme &amp; Unit Kit Plus by Fieldnote,Inc. technology.</p>
</footer>
<div class="to-top"><svg width="10" height="8" viewBox="0 0 10 8" fill="none" stroke="#fff" stroke-width="1.6"><path d="M1 7l4-5 4 5"/></svg></div>
</body>
</html>
```